nutrition ebook cover

i need a cover for a ebook designed, the book is called velvet ridge so i would like that somewhere on the cover. i would also like the word nutrition followed by my company logo that i have attached below somewhere on the cover( i have attached two logos and would like to see with both separatley), i would like this to be faded into the background if possible, perhaps in a upper or lower corner. i would also like to see options with and without the picture i have attached below. the look I'm going for is professional and clean. this is a fat loss, healthy eating booklet. the winning designer i would like to design the following pages within the book aswell no more than 10 pages, that i will provide all content for, i just need help with putting what i have on pdf in a way that looks professional and cool. this would ideally covered in the rate that is paid for the cover. i also have other booklets i need made so the winning designer will most likely get that work too at a later date for an additional fee of course.

Industry/Entity Type

Nutrition

Requirements
Nice to have
• Outside images are welcomed, happy to purchase any stock images used from a outside source

```html
<!DOCTYPE html>
<html lang="en">
<head>
<meta charset="utf-8">
<title>Velvet Ridge — Nutrition Ebook Cover</title>
<link href="https://fonts.googleapis.com/css2?family=Jost:wght@400;500&display=swap" rel="stylesheet">
<style>
  :root {
    --paper: #ffffff;
    --slate-dark: #1e2b2f;
    --slate-mid: #2f3f43;
    --wood-light: #b06a35;
    --wood-mid: #8a4a22;
    --engrave: rgba(58, 26, 8, 0.74);
    --engrave-soft: rgba(58, 26, 8, 0.62);
  }
  * { margin: 0; padding: 0; box-sizing: border-box; }
  html, body { width: 1200px; height: 1000px; overflow: hidden; background: var(--paper); }
  .cover { position: relative; width: 1200px; height: 1000px; background: var(--paper); font-family: "Jost", "Futura", sans-serif; }
  .cover-photo {
    position: absolute; left: 0; top: 40px; width: 1200px; height: 918px;
    background:
      radial-gradient(ellipse 300px 320px at 580px 540px, var(--wood-light), var(--wood-mid) 70%, transparent 100%),
      linear-gradient(135deg, var(--slate-mid), var(--slate-dark));
  }
  .title {
    position: absolute; left: 262px; top: 352px; width: 636px; text-align: center;
    color: var(--engrave); text-transform: uppercase; font-weight: 500;
  }
  .title-main { display: block; font-size: 150px; line-height: 1; letter-spacing: 0.02em; padding-left: 0.02em; }
  .title-sub { display: block; margin-top: 118px; font-size: 80px; font-weight: 400; line-height: 1; letter-spacing: 0.06em; padding-left: 0.06em; }
  .brand {
    position: absolute; left: 590px; top: 718px; height: 106px;
    display: flex; align-items: center; gap: 14px;
    color: var(--engrave-soft); font-weight: 500; text-transform: uppercase;
  }
  .brand-word { font-size: 19px; letter-spacing: 0.08em; }
  .brand-seal {
    width: 106px; height: 106px; border: 3px solid var(--engrave-soft); border-radius: 50%;
    display: flex; align-items: center; justify-content: center;
    font-size: 19px; letter-spacing: 0.04em;
  }
</style>
</head>
<body>
  <main class="cover">
    <div class="cover-photo" role="img" aria-label="Photograph of a rustic wooden chopping board on a dark slate table, surrounded by fresh vegetables — broccoli, carrot, potatoes, mushrooms, cherry tomatoes, spring onion, turnip, lemon, chillies and oil"></div>
    <h1 class="title">
      <span class="title-main">Velvet</span>
      <span class="title-sub">Ridge</span>
    </h1>
    <div class="brand">
      <span class="brand-word">Nutrition</span>
      <span class="brand-seal">Tilda Fit</span>
    </div>
  </main>
</body>
</html>
```